Vitamin Company Website Design

Seeking to create a vibrant and professional looking website for a vitamin and health food supplements business.

Morning Flintroot is a company that develops and sells vitamins and supplements for those following the "paleo" or "caveman" diet. The diet focuses upon eating organic vegetables and meat, like our ancient ancestors.

The website should emphasize health and wellness. A clean and bold design is preferred.

The website should include four sections: a home page, a blog, a community forum and an e-commerce store.

These websites communicate what we would like to look like:

http://www.korvelstudio.example/
http://www.unityassembly.example/
http://www.tlx.example/
http://www.zestkitten.example/
http://openvoiceforum.example/en/
http://tastebayoucatch.example/
http://buyrooted.example/

Target Market(s)

Health conscious men and women age 25-50

Industry/Entity Type

E-Commerce

Requirements
Must have
• The website must have 4 pages: home page, blog, community forum and online store.

The website must incorporate the company's logo, which is attached.

The company's green logo with the tagline: "Modern Wellness. Prehistoric Wisdom." is the preferred logo.

Please incorporate the other logo graphics where you see fit.
Nice to have
• Ideally, the designer will add images and/or graphics that compliment a website dedicated to health and wellness.

```html
<!DOCTYPE html>
<html lang="en">
<head>
<meta charset="utf-8">
<title>Morning Flintroot — Modern Wellness. Prehistoric Wisdom.</title>
<link rel="stylesheet" href="https://fonts.googleapis.com/css2?family=Arimo:wght@400;700&display=swap">
<style>
  :root {
    --green: #3fae2a;
    --green-light: #5cc63b;
    --green-dark: #2f9a1f;
    --text: #333333;
    --text-soft: #555555;
    --gray-bg: #f2f2f2;
    --line: #cccccc;
    --footer: #454545;
    --footer-text: #e6e6e6;
  }
  * { margin: 0; padding: 0; box-sizing: border-box; }
  html, body { width: 830px; height: 1200px; overflow: hidden; background: #ffffff; }
  body { font-family: "Arimo", Arial, sans-serif; color: var(--text); position: relative; }
  a { color: inherit; text-decoration: none; }

  .site-header {
    position: absolute; left: 0; top: 0; width: 830px; height: 107px;
    background: linear-gradient(#ffffff, #ececec);
  }
  .brand { position: absolute; left: 30px; top: 25px; display: flex; align-items: center; gap: 8px; }
  .brand-dot { width: 48px; height: 48px; border-radius: 50%; background: var(--green); }
  .brand-name { font-size: 22px; color: var(--green); font-weight: 400; line-height: 1; }
  .brand-tagline { font-size: 8px; color: #666; margin-top: 4px; }
  .utility-links { position: absolute; right: 32px; top: 9px; font-size: 8px; color: #777; }
  .utility-links .count { color: var(--green); font-weight: 700; }
  .utility-links .sep { margin: 0 4px; color: #bbb; }

  .main-nav { position: absolute; left: 355px; top: 72px; display: flex; height: 35px; }
  .main-nav a { font-size: 11px; color: var(--green); line-height: 35px; padding: 0 16px; }
  .main-nav a.active { background: #d4d4d4; color: #555; padding: 0 17px; }

  .hero { position: absolute; left: 27px; top: 107px; width: 775px; height: 283px; background: var(--gray-bg); }
  .hero-image {
    position: absolute; left: 0; top: 0; width: 470px; height: 283px;
    background: radial-gradient(ellipse at 55% 55%, #f2a53a 0%, #f0c24b 22%, #e8e8e4 55%, #eeeeee 100%);
  }
  .hero-copy { position: absolute; left: 480px; top: 60px; width: 275px; }
  .hero-copy h1 { font-size: 27px; font-weight: 400; color: var(--green); margin-bottom: 8px; }
  .hero-copy p { font-size: 12px; line-height: 15.6px; color: #333; }
  .hero-copy .learn-more { display: block; margin-top: 16px; font-size: 12px; color: #777; }

  .section-bar {
    position: absolute; height: 29px; background: linear-gradient(var(--green-light), var(--green-dark));
    color: #fff; font-size: 14px; line-height: 29px; padding-left: 15px;
  }

  .product-grid { position: absolute; left: 29px; top: 453px; width: 773px;
    display: grid; grid-template-columns: repeat(5, 143px); column-gap: 14.5px; row-gap: 16px; }
  .product-card { height: 168px; border: 1px solid var(--line); background: #fff; position: relative; }
  .product-photo { position: absolute; left: 6px; top: 7px; width: 129px; height: 126px; }
  .product-meta { position: absolute; left: 8px; right: 8px; bottom: 8px; display: flex; justify-content: space-between; font-size: 11px; color: #555; }

  .pagination { position: absolute; right: 32px; top: 821px; display: flex; gap: 1px; font-size: 11px; }
  .pagination span { width: 16px; height: 16px; line-height: 16px; text-align: center; color: #555; }
  .pagination .current { background: var(--green); color: #fff; font-weight: 700; }

  .about-copy { position: absolute; left: 39px; top: 893px; width: 360px; font-size: 9.6px; line-height: 15.6px; color: var(--text-soft); }
  .about-copy p + p { margin-top: 15px; }

  .blog-list { position: absolute; left: 433px; top: 891px; width: 360px; list-style: none; }
  .blog-item { display: flex; gap: 10px; height: 60px; }
  .blog-thumb { width: 57px; height: 43px; flex: none; }
  .blog-item p { font-size: 9.6px; line-height: 13.2px; color: var(--text-soft); }

  .button {
    position: absolute; top: 1061px; width: 93px; height: 27px; border: 1px solid #bbb;
    background: linear-gradient(#ffffff, #e4e4e4); color: var(--green); font-size: 10px;
    text-align: center; line-height: 25px;
  }

  .site-footer { position: absolute; left: 0; top: 1109px; width: 830px; height: 91px; background: var(--footer); }
  .legal { position: absolute; left: 31px; top: 42px; font-size: 8px; color: var(--footer-text); }
  .social-icons { position: absolute; left: 520px; top: 41px; display: flex; gap: 8px; }
  .social-icons span { width: 14px; height: 14px; background: #6a8fb8; border-radius: 2px; }
  .footer-divider { position: absolute; left: 671px; top: 35px; width: 1px; height: 24px; background: #666; }
  .payment-icons { position: absolute; left: 695px; top: 42px; display: flex; gap: 3px; }
  .payment-icons span { width: 19px; height: 13px; background: #dcdcdc; border-radius: 1px; }
</style>
</head>
<body>
  <header class="site-header">
    <a class="brand" href="#">
      <span class="brand-dot"></span>
      <span>
        <span class="brand-name">Morning Flintroot</span>
        <span class="brand-tagline" style="display:block">Modern Wellness. Prehistoric Wisdom.</span>
      </span>
    </a>
    <div class="utility-links"><a href="#">My Account</a><span class="sep">|</span><a href="#">Shopping Cart <span class="count">(0)</span></a></div>
    <nav class="main-nav">
      <a class="active" href="#">Home</a>
      <a href="#">About us</a>
      <a href="#">Services</a>
      <a href="#">Products</a>
      <a href="#">Recipies</a>
      <a href="#">Contact us</a>
    </nav>
  </header>

  <section class="hero">
    <div class="hero-image" role="img" aria-label="Glass of orange juice beside lemons, an orange, a lime and a spilled bottle of vitamin tablets"></div>
    <div class="hero-copy">
      <h1>Morning flintroot</h1>
      <p>Lorem Ipsum is simply dummy text of the printing and typesetting industry. Lorem Ipsum has been the industry's standard dummy text ever since the 1500s, when an unknown printer took a galley of type and scrambled it to make a type specimen book.</p>
      <a class="learn-more" href="#">Learn More</a>
    </div>
  </section>

  <h2 class="section-bar" style="left:28px;top:406px;width:774px;font-weight:400">Our Products</h2>

  <div class="product-grid">
    <div class="product-card"><div class="product-photo" role="img" aria-label="Assorted supplement capsules and softgels" style="background:linear-gradient(135deg,#f4f4f0,#d8cfa8 50%,#8a3a3a 70%,#eeeeea)"></div><div class="product-meta"><a href="#">View</a><span>| $98.00</span></div></div>
    <div class="product-card"><div class="product-photo" role="img" aria-label="Colourful chewable vitamin tablets spilling from a bottle" style="background:linear-gradient(160deg,#6a5470,#e0708a 45%,#f0a070 65%,#f2f2f2)"></div><div class="product-meta"><a href="#">View</a><span>| $98.00</span></div></div>
    <div class="product-card"><div class="product-photo" role="img" aria-label="Sliced apple and orange stacked with capsules" style="background:linear-gradient(#ffffff 5%,#8cc040 25%,#f0901e 45%,#b02a2a 60%,#8cc040 80%,#ffffff)"></div><div class="product-meta"><a href="#">View</a><span>| $98.00</span></div></div>
    <div class="product-card"><div class="product-photo" role="img" aria-label="Woven basket filled with almonds" style="background:radial-gradient(circle at 50% 45%,#b07a44,#c8aa80 55%,#ffffff 80%)"></div><div class="product-meta"><a href="#">View</a><span>| $98.00</span></div></div>
    <div class="product-card"><div class="product-photo" role="img" aria-label="Close-up of mixed amber softgels and capsules" style="background:linear-gradient(135deg,#d9a030,#8a4a14 45%,#e8c060 70%,#6a2a10)"></div><div class="product-meta"><a href="#">View</a><span>| $98.00</span></div></div>
    <div class="product-card"><div class="product-photo" role="img" aria-label="Golden fish oil softgel among tablets" style="background:radial-gradient(circle at 55% 50%,#f0c020,#d8b030 35%,#c8b070 60%,#f2f2f2)"></div><div class="product-meta"><a href="#">View</a><span>| $98.00</span></div></div>
    <div class="product-card"><div class="product-photo" role="img" aria-label="Grapes, berries and strawberries beside scattered pills" style="background:linear-gradient(160deg,#b8c070,#4a3a2a 40%,#a02030 65%,#e8e8e8)"></div><div class="product-meta"><a href="#">View</a><span>| $98.00</span></div></div>
    <div class="product-card"><div class="product-photo" role="img" aria-label="Stacked fruit slices with a blister pack of capsules" style="background:linear-gradient(135deg,#ffffff 10%,#e04020 35%,#f0a020 55%,#c03040 75%,#ffffff)"></div><div class="product-meta"><a href="#">View</a><span>| $98.00</span></div></div>
    <div class="product-card"><div class="product-photo" role="img" aria-label="Broccoli florets and halved kiwi fruit" style="background:radial-gradient(circle at 50% 60%,#8ab830,#5a8a20 35%,#ffffff 70%)"></div><div class="product-meta"><a href="#">View</a><span>| $98.00</span></div></div>
    <div class="product-card"><div class="product-photo" role="img" aria-label="Assorted supplement capsules and softgels" style="background:linear-gradient(135deg,#f4f4f0,#d8cfa8 50%,#8a3a3a 70%,#eeeeea)"></div><div class="product-meta"><a href="#">View</a><span>| $98.00</span></div></div>
  </div>

  <nav class="pagination"><span class="current">1</span><span>2</span><span>3</span><span>4</span><span>5</span></nav>

  <h2 class="section-bar" style="left:28px;top:852px;width:377px;font-weight:400">About us</h2>
  <h2 class="section-bar" style="left:424px;top:852px;width:377px;font-weight:400">Our Blog</h2>

  <div class="about-copy">
    <p>Lorem Ipsum is simply dummy text of the printing and typesetting industry. Lorem Ipsum has been the industry's standard dummy text ever since the 1500s, when an unknown printer took a galley of type and scrambled it to make a type specimen book.</p>
    <p>It has survived not only five centuries, but also the leap into electronic typesetting, remaining essentially unchanged. It was popularised in the 1960s with the release of Pressline sheets containing Lorem Ipsum passages, and more recently with desktop publishing software like Folio Layout including versions of Lorem Ipsum.</p>
  </div>

  <ul class="blog-list">
    <li class="blog-item"><div class="blog-thumb" role="img" aria-label="Blog post photo of a smiling woman" style="background:linear-gradient(135deg,#e8e4dc,#c8a888)"></div><p>Lorem Ipsum is simply dummy text of the printing and typesetting industry. Lorem Ipsum has been the industry's standard dummy text .........</p></li>
    <li class="blog-item"><div class="blog-thumb" role="img" aria-label="Blog post photo of a woman looking upward" style="background:linear-gradient(135deg,#ffffff,#e0b090 50%,#5a3a20)"></div><p>Lorem Ipsum is simply dummy text of the printing and typesetting industry. Lorem Ipsum has been the industry's standard dummy text .........</p></li>
    <li class="blog-item"><div class="blog-thumb" role="img" aria-label="Blog post photo of a woman in profile" style="background:linear-gradient(135deg,#c89060,#e8c8a8 60%,#f4f0ec)"></div><p>Lorem Ipsum is simply dummy text of the printing and typesetting industry. Lorem Ipsum has been the industry's standard dummy text &nbsp;.........</p></li>
  </ul>

  <a class="button" href="#" style="left:39px">Read More</a>
  <a class="button" href="#" style="left:430px">Read More</a>

  <footer class="site-footer">
    <p class="legal">© 2012 - Terms of Service - Privacy Policy - Program Policies</p>
    <div class="social-icons" aria-label="Social links"><span></span><span></span><span></span><span></span><span></span><span></span></div>
    <div class="footer-divider"></div>
    <div class="payment-icons" aria-label="Accepted payment methods"><span></span><span></span><span></span><span></span><span></span></div>
  </footer>
</body>
</html>
```